Business card design incorporating discount offer

We are a trade services company and we need a double sided business card that is going to be used by our tradesmen to give to customers on completion of their jobs.

Below are the key elements of the card that we would like to include:

-Main logo with text 'Expert Property Care' underneath.
-Up to 12 smaller icon logos with text 'Your local all-trade experts' to emphasise the point that we cover all the trades
-Discount offer - 10% discount
-Telephone number and website address
-Blank space for tradesman to enter his/her name
-Request for customer feedback with feedback url

This business card will be printed on regular card. In the past we have favoured designs that use a black background but we're open to new ideas.

I have attached a few files:

-A simple wire frame example to show how this card could look with the different elements mentioned above, feel free to use a layout similar to this or come up with something totally different (biz-card.pdf)
-Front and back of a loyalty card the we've used in the past (this card was printed on plastic)
-Front and back of a key fob design that we've previously used (this card was printed on plastic)
-A logo file with the 12 small icons and the main logo image

If you need further images or information please ask.

```html
<!DOCTYPE html>
<html lang="en">
<head>
<meta charset="utf-8">
<title>HLT Expert Property Care – Business Card</title>
<link rel="stylesheet" href="https://fonts.googleapis.com/css2?family=Arimo:wght@400;700&family=Bebas+Neue&display=swap">
<style>
  :root {
    --backdrop: #e8e5e1;
    --black: #000000;
    --red: #e42127;
    --red-light: #ef4a36;
    --maroon: #5f1912;
    --white: #ffffff;
    --cyan: #1ea6e0;
    --orange: #f39323;
    --sans: "Arimo", Arial, sans-serif;
    --condensed: "Bebas Neue", "Arial Narrow", sans-serif;
  }
  * { margin: 0; padding: 0; box-sizing: border-box; }
  html, body { width: 1200px; height: 1200px; overflow: hidden; }
  body { background: var(--backdrop); position: relative; font-family: var(--sans); color: var(--white); }

  .card { position: absolute; left: 180px; width: 840px; overflow: hidden; }
  .card-front { top: 26px; height: 556px; background: var(--black); }
  .card-back { top: 613px; height: 553px; background: var(--black); }

  /* front */
  .brand-name { position: absolute; left: 48px; top: 120px; font-size: 108px; font-weight: 700; letter-spacing: 2px; line-height: 1; }
  .brand-tagline { position: absolute; left: 48px; top: 300px; font-size: 43px; font-weight: 700; line-height: 1; }
  .divider { position: absolute; left: 0; top: 410px; width: 574px; height: 4px; background: var(--red); }

  .contact { position: absolute; left: 46px; font-size: 27px; display: flex; align-items: center; gap: 14px; }
  .contact-phone { top: 448px; }
  .contact-web { top: 497px; color: var(--orange); }
  .contact svg { width: 26px; height: 26px; flex: none; }

  .offer-panel { position: absolute; left: 574px; top: 0; width: 266px; height: 414px; background: linear-gradient(128deg, var(--red-light) 0 48%, var(--red) 48% 100%); text-align: center; }
  .offer-value { position: absolute; left: 0; right: 0; top: 143px; font-size: 116px; font-weight: 700; line-height: 1; letter-spacing: -2px; }
  .offer-label { position: absolute; left: 0; right: 0; top: 246px; font-size: 46px; line-height: 1; }
  .offer-note { position: absolute; left: 0; right: 0; top: 296px; font-size: 21px; line-height: 1; }
  .offer-footer { position: absolute; left: 574px; top: 414px; width: 266px; height: 142px; background: var(--maroon); text-align: center; font-size: 21px; line-height: 31px; padding-top: 34px; letter-spacing: 0.5px; }
  .offer-pointer { position: absolute; left: 680px; top: 413px; width: 48px; height: 22px; }

  /* back */
  .trade-icons { position: absolute; left: 32px; top: 30px; display: grid; grid-template-columns: 74px 74px; column-gap: 14px; row-gap: 11px; }
  .trade-tile { width: 74px; height: 74px; border-radius: 11px; background-image: linear-gradient(180deg, rgba(255,255,255,.28) 0 45%, rgba(0,0,0,.06) 45% 100%); box-shadow: inset 0 0 0 2px rgba(0,0,0,.25); }
  .tile-carpentry { background-color: #b7834d; }
  .tile-joinery { background-color: #dfa52a; }
  .tile-plumbing { background-color: #1c7ec4; }
  .tile-bathrooms { background-color: #9c3f99; }
  .tile-building { background-color: #1f6db5; }
  .tile-drainage { background-color: #5e6d7b; }
  .tile-maintenance { background-color: #e9cf3e; }
  .tile-electrics { background-color: #8d8d8d; }
  .tile-appliances { background-color: #3bb4ae; }
  .tile-gas { background-color: #1b8ad2; }
  .tile-decorating { background-color: #e23c3c; }
  .tile-pest-control { background-color: #7db444; }

  .back-main { position: absolute; left: 232px; top: 0; width: 608px; height: 553px; background: var(--red); }
  .back-header { position: absolute; left: 0; top: 0; width: 608px; height: 143px; background: var(--maroon); text-align: center; font-family: var(--condensed); font-size: 49px; line-height: 1; padding-top: 53px; letter-spacing: 0.5px; }
  .back-pointer { position: absolute; left: 280px; top: 142px; width: 48px; height: 22px; }

  .tradesman-label { position: absolute; left: 26px; top: 222px; font-size: 20px; }
  .tradesman-field { position: absolute; left: 26px; top: 251px; width: 556px; height: 55px; background: var(--white); }

  .feedback { position: absolute; left: 0; right: 0; text-align: center; line-height: 1; }
  .feedback-question { top: 355px; font-size: 30px; }
  .feedback-request { top: 400px; font-size: 24px; }
  .feedback-url { top: 438px; font-size: 31px; }
  .rating-stars { top: 490px; font-size: 25px; letter-spacing: 3px; }
</style>
</head>
<body>

<section class="card card-front" aria-label="Card front">
  <div class="brand-name">HLT</div>
  <div class="brand-tagline">Expert Property Care</div>
  <div class="divider"></div>

  <div class="contact contact-phone">
    <svg viewBox="0 0 24 24" aria-hidden="true"><path fill="#1ea6e0" d="M3 9c0-2 2-4 9-4s9 2 9 4v2h-5V9H8v2H3zM6 12h12l2 7H4zm6 1.5a2.5 2.5 0 1 0 0 5 2.5 2.5 0 0 0 0-5z"/></svg>
    <span>0800 123 4567</span>
  </div>
  <div class="contact contact-web">
    <svg viewBox="0 0 24 24" aria-hidden="true"><circle cx="11" cy="11" r="8" fill="none" stroke="#1ea6e0" stroke-width="2"/><path d="M3 11h16M11 3c-3 3-3 13 0 16M11 3c3 3 3 13 0 16" fill="none" stroke="#1ea6e0" stroke-width="1.6"/><path fill="#1ea6e0" d="M14 14l8 3-3.5 1.2L17 22z"/></svg>
    <span>www.hlt-homecare.co.uk</span>
  </div>

  <div class="offer-panel">
    <div class="offer-value">%10</div>
    <div class="offer-label">Discount</div>
    <div class="offer-note">With this card</div>
  </div>
  <div class="offer-footer">Check our&nbsp; website&nbsp; for<br>full offer details</div>
  <svg class="offer-pointer" viewBox="0 0 48 22" aria-hidden="true"><polygon points="0,0 48,0 24,22" fill="#e42127"/></svg>
</section>

<section class="card card-back" aria-label="Card back">
  <div class="trade-icons">
    <div class="trade-tile tile-carpentry" role="img" aria-label="Carpentry trade icon"></div>
    <div class="trade-tile tile-joinery" role="img" aria-label="Joinery trade icon"></div>
    <div class="trade-tile tile-plumbing" role="img" aria-label="Plumbing trade icon"></div>
    <div class="trade-tile tile-bathrooms" role="img" aria-label="Bathrooms trade icon"></div>
    <div class="trade-tile tile-building" role="img" aria-label="Building trade icon"></div>
    <div class="trade-tile tile-drainage" role="img" aria-label="Drainage trade icon"></div>
    <div class="trade-tile tile-maintenance" role="img" aria-label="Maintenance trade icon"></div>
    <div class="trade-tile tile-electrics" role="img" aria-label="Electrics trade icon"></div>
    <div class="trade-tile tile-appliances" role="img" aria-label="Appliances trade icon"></div>
    <div class="trade-tile tile-gas" role="img" aria-label="Gas trade icon"></div>
    <div class="trade-tile tile-decorating" role="img" aria-label="Decorating trade icon"></div>
    <div class="trade-tile tile-pest-control" role="img" aria-label="Pest control trade icon"></div>
  </div>

  <div class="back-main">
    <div class="back-header">Your local all-trade experts</div>
    <svg class="back-pointer" viewBox="0 0 48 22" aria-hidden="true"><polygon points="0,0 48,0 24,22" fill="#5f1912"/></svg>

    <div class="tradesman-label">Your HLT tradesman :</div>
    <div class="tradesman-field"></div>

    <div class="feedback feedback-question">What do you think of our service?</div>
    <div class="feedback feedback-request">Please leave feedback online</div>
    <div class="feedback feedback-url">www.hlt-homecare.co.uk/feedback</div>
    <div class="feedback rating-stars" aria-label="Rating stars">★★★★★★★★★★</div>
  </div>
</section>

</body>
</html>
```